Tallowreed Advisory Partners Business Card Design

We have the logo we just need someone to design a modern business card design.

Name: Desmond Munkalt
Phone: 3055550148
Mobile: 9175550193
Web:www.tallowreedadvisory.example
email: dmunkalt@tallowreedadvisory.example
Company: Tallowreed Advisory Partners
Title: CEO

Address: 718 Quillmore Ave, Miami, Florida 33190

Target Market(s)

companies over 100 employees

Industry/Entity Type

Business

```html
<!DOCTYPE html>
<html lang="en">
<head>
<meta charset="utf-8">
<title>Tallowreed Advisory Partners – Business Card</title>
<link rel="stylesheet" href="https://fonts.googleapis.com/css2?family=Arimo:wght@400;700&display=swap">
<style>
  :root {
    --page: #e4e4e2;
    --card-black: #111111;
    --brand-blue: #1474bd;
    --deep-blue: #2f5a8c;
    --white: #ffffff;
    --muted-grey: #6f6f6f;
    --shadow: rgba(0, 0, 0, 0.18);
  }
  * { box-sizing: border-box; margin: 0; padding: 0; }
  html, body {
    width: 1200px; height: 900px; overflow: hidden;
    background: var(--page);
    font-family: "Arimo", Arial, sans-serif;
  }
  .sheet {
    width: 1200px; height: 900px;
    display: flex; flex-direction: column; align-items: center; justify-content: center;
    gap: 40px;
  }
  .card {
    position: relative;
    width: 680px; height: 389px;
    overflow: hidden;
    box-shadow: 0 6px 18px var(--shadow);
    background: var(--card-black);
  }

  /* ---------- Front ---------- */
  .front-band {
    position: absolute; left: 0; right: 0; bottom: 0; height: 60px;
    background: var(--brand-blue);
    border-top: 7px solid var(--white);
  }
  .front-brand {
    position: absolute; left: 0; right: 0; top: 40px;
    display: flex; flex-direction: column; align-items: center;
  }
  .brand-dot {
    width: 110px; height: 110px; border-radius: 50%;
    background: var(--brand-blue);
  }
  .front-name {
    margin-top: 22px;
    color: var(--white);
    font-weight: 700;
    text-align: center;
    line-height: 1.05;
  }
  .front-name .line-main { display: block; font-size: 52px; letter-spacing: 3px; }
  .front-name .line-sub { display: block; font-size: 20px; letter-spacing: 2px; margin-top: 4px; }

  /* ---------- Back ---------- */
  .card.back { background: var(--white); }
  .back-identity {
    position: absolute; left: 0; top: 0; width: 262px; height: 334px;
    background: var(--card-black);
    display: flex; flex-direction: column; align-items: center;
  }
  .back-identity .brand-dot { width: 150px; height: 150px; margin-top: 30px; }
  .person-name {
    margin-top: 70px;
    color: var(--white); font-weight: 700; font-size: 28px;
  }
  .person-title {
    margin-top: 12px;
    color: var(--muted-grey); font-size: 20px;
  }
  .back-header {
    position: absolute; left: 274px; right: 0; top: 0; height: 56px;
    background: var(--deep-blue);
  }
  .back-contact {
    position: absolute; left: 274px; right: 0; top: 64px; height: 262px;
    background: var(--brand-blue);
    color: var(--white);
    padding: 22px 0 0 30px;
    font-size: 17px;
  }
  .contact-row { display: flex; align-items: center; gap: 8px; line-height: 1; }
  .contact-row + .contact-row { margin-top: 11px; }
  .contact-row .pair { display: flex; align-items: center; gap: 8px; margin-right: 18px; }
  .icon { width: 18px; height: 18px; flex: none; }
  .address { margin: 28px 0 0 26px; line-height: 1.35; }
  .company-lines { margin-top: 40px; }
  .back-band {
    position: absolute; left: 0; right: 0; bottom: 0; height: 48px;
    background: var(--brand-blue);
    border-top: 7px solid var(--white);
  }
</style>
</head>
<body>
<main class="sheet">

  <section class="card front" aria-label="Card front">
    <div class="front-brand">
      <div class="brand-dot"></div>
      <p class="front-name">
        <span class="line-main">TALLOWREED</span>
        <span class="line-sub">ADVISORY PARTNERS</span>
      </p>
    </div>
    <div class="front-band"></div>
  </section>

  <section class="card back" aria-label="Card back">
    <div class="back-identity">
      <div class="brand-dot"></div>
      <p class="person-name">Desmond Munkalt</p>
      <p class="person-title">CEO</p>
    </div>

    <div class="back-header"></div>

    <div class="back-contact">
      <div class="contact-row">
        <span class="pair">
          <svg class="icon" viewBox="0 0 20 20"><circle cx="10" cy="10" r="10" fill="#fff"/><path d="M6.5 5.2l2 .2.6 2.4-1.2 1a7 7 0 0 0 3.3 3.3l1-1.2 2.4.6.2 2c-5 .8-9.1-3.3-8.3-8.3z" fill="#1474bd"/></svg>
          305 555 0148
        </span>
        <span class="pair">
          <svg class="icon" viewBox="0 0 20 20"><rect x="5" y="1" width="10" height="18" rx="2" fill="none" stroke="#fff" stroke-width="1.6"/><circle cx="10" cy="16" r="1" fill="#fff"/></svg>
          917 555 0193
        </span>
      </div>
      <div class="contact-row">
        <svg class="icon" viewBox="0 0 20 20"><rect x="1.5" y="4" width="17" height="12" fill="none" stroke="#fff" stroke-width="1.6"/><path d="M1.5 4.5l8.5 6.5 8.5-6.5" fill="none" stroke="#fff" stroke-width="1.6"/></svg>
        dmunkalt@tallowreedadvisory.example
      </div>

      <p class="address">718 Quillmore Ave<br>Miami, Florida 33190</p>

      <div class="company-lines">
        <div class="contact-row">
          <svg class="icon" viewBox="0 0 20 20"><rect x="1.5" y="4" width="17" height="12" fill="none" stroke="#fff" stroke-width="1.6"/><path d="M1.5 4.5l8.5 6.5 8.5-6.5" fill="none" stroke="#fff" stroke-width="1.6"/></svg>
          info@tallowreedadvisory.example
        </div>
        <div class="contact-row">
          <svg class="icon" viewBox="0 0 20 20"><circle cx="10" cy="10" r="8.2" fill="none" stroke="#fff" stroke-width="1.6"/><ellipse cx="10" cy="10" rx="3.6" ry="8.2" fill="none" stroke="#fff" stroke-width="1.4"/><path d="M2 10h16" stroke="#fff" stroke-width="1.4"/></svg>
          www.tallowreedadvisory.example
        </div>
      </div>
    </div>

    <div class="back-band"></div>
  </section>

</main>
</body>
</html>
```